Design a clean and bold corporate Presentation for Brand New Company

Task Outline
Create corporate presentation

Task Description
Creation of Powerpoint corporate presentation using the content below.

The presentation is 10 slides long.

PLEASE NOTE: THE FULL CONTENT AND STRUCTURE OF THE CORPORATE PRESENTATION ARE INCLUDED IN ATTACHMENT.

Corporate presentation
– structure is as attached in file titled “plumvo Corp Pres”.

We would like a clean, modern presentation with the use of graphics (not photos) to support key points. We need the graphics designed – NOT clip-art, as we aim to use these on the web-site (examples of preferred design below).

plumvo is a new start-up company where we aim to combine the best of recruitment and IT service delivery expertise to:

Offer access to the best possible resources in the UK and Globally, in a range of commercial models that offer cost savings and agility. Using best practice service delivery to assure quality.

Our foundations are outstanding employee satisfaction, and fantastic customer service.

Do’s
- Be bold ! Use clean design graphics to better highlight and explain products and capabilities in the corporate presentation
- Professional, contemporary and clean – our target market are new IT businesses that are web-savvy.
- Use single colour graphics
- Use a consistent theme through-out
- Establish a design that would translate easily to the web
- Establish a design that would translate into a Powerpoint template
- Use Calibri font

Don’ts
- Use generic photos e.g. “smiling IT professional” ;-)
- No cartoon graphics
- Use complex multi-colour graphics
- Use standard Powerpoint clip-art
- Create a large file
- Use animation / transitions

Output
Powerpoint file – 2011 but compatible with 2007

Deadline
+ 1 week from issue.

What is your industry?
IT Recruitment, Consulting, Professional Services

Target Market
• New customers - Our target market are high growth companies with a heavy reliance on IT, 50-250 employees, based in UK.
• Hiring candidates – IT professionals who are potential hiring candidates for our customers.
• Employees – typically graduates who will be looking for their first/second professional role

What design styles do you like that you would like to reflect in the design?
• http://www.qrtl.com/what-we-offer/
• http://www.zenthic.io/platform-as-a-service/zenthic-sky-harbor
• www.lumo.com

Do you have any other info or links you want to share?
- Corporate presentation
- Logo image

Target Market(s)

Target Market

Industry/Entity Type

It Company

Font styles to use
Sans Serif

Colors
34a6d7
faa54b
d2a4cc
85acd3

Requirements
Must have
• Do’s
• - Be bold ! Use clean design graphics to better highlight and explain products and capabilities in the corporate presentation
• - Professional, contemporary and clean – our target market are new IT businesses that are web-savvy.
• - Use single colour graphics
• - Use a consistent theme through-out
• - Establish a design that would translate easily to the web
• - Establish a design that would translate into a Powerpoint template
• - Use Calibri font
Nice to have
• Use of transparent background imagery
Should not have
• Don’ts
• - Use generic photos e.g. “smiling IT professional” ;-)
• - No cartoon graphics
• - Use complex multi-colour graphics
• - Use standard Powerpoint clip-art
• - Create a large file
• - Use animation / transitions

```html
<!DOCTYPE html>
<html lang="en">
<head>
<meta charset="utf-8">
<title>plumvo – Resourcing</title>
<link href="https://fonts.googleapis.com/css2?family=Carlito:wght@400;700&display=swap" rel="stylesheet">
<style>
  :root {
    --navy: #1f3f87;
    --orange: #f47a17;
    --footer-orange: #f26b12;
    --text-grey: #5a5a5a;
    --tab-grey: #d9d9d9;
    --tab-edge: #eeeeee;
    --white: #ffffff;
    --bg-soft: #f2f2f2;
  }
  * { margin: 0; padding: 0; box-sizing: border-box; }
  html, body { width: 1200px; height: 900px; overflow: hidden; }
  body { font-family: "Carlito", "Calibri", sans-serif; background: var(--white); }

  .slide {
    position: relative;
    width: 1200px;
    height: 900px;
    overflow: hidden;
    background:
      radial-gradient(circle at 120px 420px, rgba(0,0,0,0.045) 0, rgba(0,0,0,0.03) 260px, transparent 420px),
      radial-gradient(circle at 1050px 200px, rgba(0,0,0,0.03) 0, transparent 320px),
      linear-gradient(135deg, var(--bg-soft) 0%, var(--white) 55%, var(--white) 100%);
  }

  .section-tab {
    position: absolute;
    left: 0;
    top: 18px;
    width: 303px;
    height: 75px;
    background: linear-gradient(180deg, var(--tab-edge) 0%, var(--tab-grey) 100%);
    border-radius: 0 14px 14px 0;
    box-shadow: 0 2px 3px rgba(0,0,0,0.12);
    display: flex;
    align-items: center;
    padding-left: 26px;
  }
  .section-tab__label {
    color: var(--navy);
    font-weight: 700;
    font-size: 37px;
    letter-spacing: 0.5px;
  }

  .brand {
    position: absolute;
    right: 36px;
    top: 34px;
    display: flex;
    align-items: center;
    gap: 10px;
  }
  .brand__mark {
    width: 18px;
    height: 18px;
    background: var(--orange);
  }
  .brand__name {
    color: var(--navy);
    font-weight: 700;
    font-size: 50px;
    line-height: 1;
  }

  .headline {
    position: absolute;
    left: 63px;
    top: 268px;
    color: var(--navy);
    font-weight: 700;
    font-size: 31px;
  }

  .points {
    position: absolute;
    left: 117px;
    top: 374px;
    list-style: none;
  }
  .points__item {
    display: flex;
    align-items: center;
    height: 48px;
    margin-bottom: 54px;
    color: var(--text-grey);
    font-size: 35px;
  }
  .points__bullet {
    width: 16px;
    height: 16px;
    border-radius: 50%;
    background: var(--orange);
    margin-right: 35px;
    flex-shrink: 0;
  }

  .illustration {
    position: absolute;
    left: 925px;
    top: 380px;
    width: 270px;
    height: 250px;
    border-radius: 12px;
    background: linear-gradient(160deg, #6a9be0 0%, #f2a65a 55%, #e6e6e6 100%);
    opacity: 0.85;
  }

  .footer {
    position: absolute;
    left: 0;
    bottom: 0;
    width: 1200px;
    height: 42px;
    background: var(--footer-orange);
  }
  .footer__copyright {
    position: absolute;
    left: 12px;
    bottom: 9px;
    color: var(--white);
    font-size: 18px;
  }
  .page-tab {
    position: absolute;
    right: 0;
    bottom: 0;
    width: 102px;
    height: 78px;
  }
  .page-tab__number {
    position: absolute;
    right: 38px;
    bottom: 11px;
    color: var(--white);
    font-weight: 700;
    font-size: 27px;
  }
</style>
</head>
<body>
  <main class="slide">
    <div class="section-tab"><span class="section-tab__label">RESOURCING</span></div>

    <div class="brand">
      <span class="brand__mark"></span>
      <span class="brand__name">plumvo</span>
    </div>

    <h1 class="headline">We wanted to do something different….</h1>

    <ul class="points">
      <li class="points__item"><span class="points__bullet"></span>Always deliver.</li>
      <li class="points__item"><span class="points__bullet"></span>Charge less, for doing more.</li>
      <li class="points__item"><span class="points__bullet"></span>Bring some rigour.</li>
    </ul>

    <div class="illustration" role="img" aria-label="Illustration of a blue and orange rocket launching beside two small grey figures"></div>

    <footer class="footer">
      <span class="footer__copyright">Copyright text here</span>
    </footer>
    <svg class="page-tab" viewBox="0 0 102 78" aria-hidden="true">
      <path d="M0 78 L0 58 C0 48 8 42 18 43 C20 30 32 24 44 28 C50 18 66 16 74 26 C84 22 96 28 98 38 L102 38 L102 78 Z" fill="var(--footer-orange)"/>
    </svg>
    <span class="page-tab__number">01</span>
  </main>
</body>
</html>
```